LHW TMA Website

Would like to have a website created that keeps with the branding of our other company; Larkfield Harbor Corporation. www.larkfieldharbor.net

Target Market(s)

Medical providers, accounts receivable management

Industry/Entity Type

Accounts Receivable Management

Number of Pages Required

5+ page

Requirements
Must have
• look similar to www.larkfieldharbor.net, but will have different logo and domain as it is completely separate company

```html
<!DOCTYPE html>
<html lang="en">
<head>
<meta charset="UTF-8">
<title>LHW TMA – Extended Business Office Services</title>
<link href="https://fonts.googleapis.com/css2?family=Montserrat:wght@300;400;500;600;700&family=Lato:ital,wght@0,400;0,700;0,900;1,400&display=swap" rel="stylesheet">
<style>
:root{
  --blue:#175a8a;
  --green:#1e8a2c;
  --green-text:#2b8a31;
  --maroon:#8a4b4c;
  --mint:#7fb9a1;
  --slate:#82aab3;
  --ink:#444;
  --muted:#555;
  --light:#f5f5f5;
  --white:#fff;
  --black:#000;
}
*{margin:0;padding:0;box-sizing:border-box}
html,body{width:1200px;height:3074px;overflow:hidden}
body{position:relative;font-family:'Lato',sans-serif;color:var(--ink);background:var(--white)}
.abs{position:absolute}
.brand{font-family:'Montserrat',sans-serif;font-weight:700;color:var(--white);font-size:37px;letter-spacing:1px;line-height:1}
.btn{position:absolute;display:flex;align-items:center;justify-content:center;background:var(--green);color:var(--white);border-radius:24px;font-family:'Lato',sans-serif;font-weight:900;font-size:13.5px;text-transform:uppercase;letter-spacing:.3px}
.nav{display:flex;gap:30px;font-weight:700;font-size:13px;color:var(--white);text-transform:uppercase}

/* hero */
.hero{left:0;top:0;width:1200px;height:600px;background:linear-gradient(135deg,#4a5058 0%,#2d3239 40%,#3c3a38 70%,#585048 100%)}
.hero-title{left:75px;top:174px;font-family:'Montserrat',sans-serif;font-weight:300;font-size:66px;line-height:78px;color:var(--white)}
.hero-lede{left:81px;top:342px;font-size:15px;line-height:28px;color:var(--white)}
.service-diagram{left:589px;top:145px;width:530px;height:360px;border-radius:18px;background:linear-gradient(100deg,var(--maroon) 0%,var(--mint) 50%,var(--slate) 100%);opacity:.9}

/* section heads */
.head{position:absolute;left:0;width:1200px;text-align:center;font-family:'Montserrat',sans-serif;font-weight:300;font-size:34px;color:var(--blue);text-transform:uppercase;letter-spacing:.5px}
.rule{position:absolute;left:538px;width:124px;height:2px;background:var(--green)}

/* services */
.services-sub{left:0;width:1200px;text-align:center;top:746px;font-size:16.5px;color:var(--green-text)}
.card{position:absolute;top:798px;width:305px;height:380px;background:var(--white);box-shadow:0 2px 6px rgba(0,0,0,.22)}
.card .photo{position:absolute;left:4px;top:2px;width:297px;height:214px}
.card h3{position:absolute;left:0;top:236px;width:100%;text-align:center;font-family:'Montserrat',sans-serif;font-weight:500;font-size:17px;color:var(--blue)}
.card .dash{position:absolute;left:138px;top:265px;width:29px;height:3px;background:var(--green)}
.card p{position:absolute;left:20px;top:278px;width:265px;text-align:center;font-size:14px;line-height:28px;color:var(--ink)}
.arrow{position:absolute;top:864px;width:44px;height:44px;border-radius:50%;background:var(--white);box-shadow:0 1px 5px rgba(0,0,0,.25)}

/* about */
.about-photo{left:0;top:1259px;width:600px;height:569px;background:linear-gradient(160deg,#c9cdd2 0%,#8a8f96 45%,#3b4048 100%)}
.about{left:600px;top:1259px;width:600px;height:569px;background:var(--blue)}
.about h2{position:absolute;left:77px;top:72px;font-family:'Montserrat',sans-serif;font-weight:300;font-size:33px;color:var(--white)}
.about .line{position:absolute;left:51px;top:124px;width:123px;height:1px;background:rgba(255,255,255,.35)}
.about p{position:absolute;left:51px;top:146px;width:462px;font-size:14px;line-height:28px;color:var(--white)}
.about .more{left:51px;top:448px;width:154px;height:43px}

/* testimonials */
.quote{left:200px;top:1982px;width:800px;text-align:center;font-style:italic;font-size:15px;line-height:28px;color:var(--muted)}
.author{left:0;top:2080px;width:1200px;text-align:center;font-family:'Montserrat',sans-serif;font-weight:500;font-size:15px;color:var(--green-text);text-transform:uppercase}

/* contact */
.contact{left:0;top:2177px;width:1200px;height:521px;background:var(--light)}
.field{position:absolute;background:var(--white);border:1px solid #9a9a9a;border-radius:4px;font-size:12px;color:#333;padding:13px 16px}
.submit{left:523px;top:2575px;width:154px;height:43px}

/* footer */
.footer{left:0;top:2698px;width:1200px;height:376px;background:var(--black)}
.footer .brand{left:0;width:1200px;text-align:center;top:80px}
.footer .nav{left:0;width:1200px;justify-content:center;top:134px}
.subscribe{position:absolute;left:316px;top:179px;width:555px;height:54px;background:var(--white);border-radius:27px;font-size:16px;color:#555;padding:17px 30px}
.send{position:absolute;right:7px;top:6px;width:42px;height:42px;border-radius:50%;background:var(--green)}
.copy{left:0;width:1200px;text-align:center;top:257px;font-family:'Montserrat',sans-serif;font-size:12px;color:var(--white)}
.contact-icon{position:absolute;top:302px;width:30px;height:30px;border-radius:50%;background:var(--blue)}
</style>
</head>
<body>

<header class="abs hero" role="img" aria-label="Photo of business people shaking hands"></header>
<div class="abs brand" style="left:131px;top:24px">LHW TMA</div>
<nav class="abs nav" style="left:366px;top:35px">
  <span>Pay Now</span><span>For Consumers</span><span>Contact Us</span><span>About Us</span><span>LH Blog</span>
</nav>
<div class="btn" style="left:913px;top:20px;width:153px;height:45px">Client Login</div>
<h1 class="abs hero-title">Experience and<br>Proven Results</h1>
<p class="abs hero-lede">Extended Business Office Services and Business Debt Collection for<br>Healthcare and Commercial AR Management</p>
<div class="btn" style="left:81px;top:415px;width:154px;height:43px">Get Started</div>
<div class="abs service-diagram" role="img" aria-label="Branded diagram of service areas: healthcare AR management, commercial AR management and insurance overpayment recovery"></div>

<!-- services -->
<h2 class="head" style="top:675px">Customizable Services</h2>
<div class="rule" style="top:727px"></div>
<p class="abs services-sub">Some of our Extended Business Office Solutions and Business Debt Collection Services:</p>

<article class="card" style="left:125px">
  <div class="photo" role="img" aria-label="Photo of colleagues reviewing documents at a desk" style="background:linear-gradient(135deg,#b9c7d6,#6f8399)"></div>
  <h3>Self-Pay AR Management</h3><div class="dash"></div>
  <p>Lorem ipsum dolor sit amet, consectetur adipiscing elit, sed do eiusmod tempor incididunt ut labore et dolore.</p>
</article>
<article class="card" style="left:448px">
  <div class="photo" role="img" aria-label="Photo of a contract being signed next to a laptop" style="background:linear-gradient(135deg,#e3e6e8,#8d949c)"></div>
  <h3>Letter/Statement Service</h3><div class="dash"></div>
  <p>Lorem ipsum dolor sit amet, consectetur adipiscing elit, sed do eiusmod tempor incididunt ut labore et dolore.</p>
</article>
<article class="card" style="left:770px">
  <div class="photo" role="img" aria-label="Photo of a hand holding a light bulb over stacked coins" style="background:linear-gradient(135deg,#c9ccc8,#6e6a62)"></div>
  <h3>Third Party Billing Solutions</h3><div class="dash"></div>
  <p>Lorem ipsum dolor sit amet, consectetur adipiscing elit, sed do eiusmod tempor incididunt ut labore et dolore.</p>
</article>

<div class="arrow" style="left:106px"><svg width="44" height="44" viewBox="0 0 44 44"><path d="M25 15 L18 22 L25 29" fill="none" stroke="var(--blue)" stroke-width="3" stroke-linecap="round" stroke-linejoin="round"/></svg></div>
<div class="arrow" style="left:1050px"><svg width="44" height="44" viewBox="0 0 44 44"><path d="M19 15 L26 22 L19 29" fill="none" stroke="var(--blue)" stroke-width="3" stroke-linecap="round" stroke-linejoin="round"/></svg></div>

<!-- about -->
<div class="abs about-photo" role="img" aria-label="Photo of a smiling team stacking hands over a laptop"></div>
<section class="abs about">
  <h2>ABOUT LHW TMA</h2>
  <div class="line"></div>
  <p>The founder, Dean Whitford, already had 18 years in the company debt collections industry, working with small business, medium, large and growing agencies, as well as developed associations with many of the leaders in the field. We pride ourselves on excellent client service. We have specialized medical and commercial debt collectors assigned to your accounts that know your business best. We provide collectors with all the key details of your product/service, as well as the specific manner in which you'd like your accounts to be handled.Knowing a strong, successful company is a matter of assembling the right components; Larkfield Harbor hires top-notch company debt collection .</p>
  <div class="btn more">Learn More</div>
</section>

<!-- testimonials -->
<h2 class="head" style="top:1904px">Our Client Testimonials</h2>
<div class="rule" style="top:1955px"></div>
<p class="abs quote">I could not be happier with the work Larkfield Harbor performs for us as our EBO / Outside Collection Agency. We have had several EBOs / Outside Collection Agencies and without a doubt, LHW has outperformed them all! I highly recommend LHW and am glad to have them as partner.</p>
<p class="abs author">Marcus Dalton. NBR. Employer Services Collections Manager</p>

<!-- contact -->
<section class="abs contact"></section>
<h2 class="head" style="top:2249px">Get In Touch</h2>
<div class="rule" style="top:2300px"></div>
<div class="field" style="left:229px;top:2326px;width:366px;height:43px">First name</div>
<div class="field" style="left:606px;top:2326px;width:366px;height:43px">Last name</div>
<div class="field" style="left:229px;top:2381px;width:366px;height:43px">Email</div>
<div class="field" style="left:606px;top:2381px;width:366px;height:43px">Phone</div>
<div class="field" style="left:229px;top:2437px;width:743px;height:106px">Message</div>
<div class="btn submit">Submit</div>

<!-- footer -->
<footer class="abs footer">
  <div class="abs brand">LHW TMA</div>
  <nav class="abs nav"><span>Pay Now</span><span>For Consumers</span><span>Contact Us</span><span>About Us</span><span>LH Blog</span></nav>
  <div class="subscribe">Enter The Email
    <div class="send"><svg width="42" height="42" viewBox="0 0 42 42"><path d="M12 21 L30 13 L25 30 L21 23 Z" fill="var(--white)"/></svg></div>
  </div>
  <p class="abs copy">© Copyrights 2021 LHW TMA &nbsp; | &nbsp; All Rights Reserved</p>
  <div class="contact-icon" style="left:512px" aria-label="Email"><svg width="30" height="30" viewBox="0 0 30 30"><rect x="8" y="10" width="14" height="10" rx="1" fill="none" stroke="var(--white)" stroke-width="1.6"/><path d="M8.5 10.5 L15 16 L21.5 10.5" fill="none" stroke="var(--white)" stroke-width="1.6"/></svg></div>
  <div class="contact-icon" style="left:556px" aria-label="Phone"><svg width="30" height="30" viewBox="0 0 30 30"><path d="M11 8 L13.5 8 L14.5 12 L12.8 13.2 A9 9 0 0 0 16.8 17.2 L18 15.5 L22 16.5 L22 19 A2 2 0 0 1 20 21 A12 12 0 0 1 9 10 A2 2 0 0 1 11 8 Z" fill="var(--white)"/></svg></div>
  <div class="contact-icon" style="left:600px" aria-label="Location"><svg width="30" height="30" viewBox="0 0 30 30"><path d="M15 22 C11 17 10 15 10 13 A5 5 0 0 1 20 13 C20 15 19 17 15 22 Z" fill="var(--white)"/><circle cx="15" cy="13" r="1.8" fill="var(--blue)"/></svg></div>
  <div class="contact-icon" style="left:644px" aria-label="Website"><svg width="30" height="30" viewBox="0 0 30 30"><circle cx="15" cy="15" r="7" fill="none" stroke="var(--white)" stroke-width="1.5"/><ellipse cx="15" cy="15" rx="3" ry="7" fill="none" stroke="var(--white)" stroke-width="1.3"/><path d="M8 15 H22" stroke="var(--white)" stroke-width="1.3"/></svg></div>
</footer>

</body>
</html>
```